依頼概要
■依頼の目的/概要
弊社が販売しているフルーツトマト(高糖度トマト)のパッケージのラベルデザインをお願いします。

■依頼詳細
弊社はトマトの栽培をしています。場所は長崎県壱岐市で玄界灘の島です。
ルドワン栽培というフィルムで栽培する新しい栽培方法です。島内のスーパーで販売しており大変好評です。糖度が8度以上あり、小さな子供さんからお年寄りまで喜んで食べて頂いています。トマト嫌いの人もこのトマトなら食べれるといって食べる方もいらっしゃいます。予想以上の好評で今回栽培面積を増やし関東への販路を考えております。これまで「ぽっけるん」(子供が美味しくてパクパク食べてすぐ無くなり、また買ってと何回もせがまれママを泣かせる)というネーミングで販売していましたが。関東進出を期にネーミングを「彩穂珠」又は「さほ珠」にバージョンアップして、新しいラベルの作成を企画しております。
<ラベルの仕様>
1.トマト1粒が20g~40gのミディートマトを150g~250gのパッケージで販売することを想定して、そのパッケージに貼るラベルです。
2.ラベルの大きさは、36×45角丸5R (mm)
3.ラベルに盛込む内容は添付ファイルの内容と同じで「ぽっけるん」を「彩穂珠」又は「さほ珠」に変更(デザインにマッチする方を選択して下さい)

■その他要望
高品質が売りですから、高級感と「一目で食べてみたい」と思うようなラベルにして欲しい。ネーミングは変更しない方がいいという方は「ぽっけるん」のままでも構いません。
■ 選んだ理由

1.産地壱岐が強調されたデザインである。
2.表現したい項目が全て網羅されている。
3.デザインがシンプルでわかり易い。

■ 提案者全員のお礼・コメント

ラベルデザインの依頼は初めてでしたが、沢山のご提案を
頂き感謝しております。
多くの方のご提案有難うございました。

```html
<!DOCTYPE html>
<html lang="ja">
<head>
<meta charset="utf-8">
<title>さほ珠 ラベル</title>
<link rel="stylesheet" href="https://fonts.googleapis.com/css2?family=Kaisei+Tokumin:wght@700;800&family=Shippori+Mincho+B1:wght@700;800&display=swap">
<style>
  :root {
    --tomato-red: #d8281c;
    --tomato-deep: #8e0f08;
    --tomato-light: #f25a40;
    --label-white: #f7f7f5;
    --label-black: #050505;
    --gold-light: #e8cc8a;
    --gold-dark: #a57a35;
    --ink-dark: #111111;
    --text-white: #ffffff;
  }
  * { margin: 0; padding: 0; box-sizing: border-box; }
  html, body { width: 1200px; height: 879px; overflow: hidden; background: #ffffff; }
  .canvas { position: relative; width: 1200px; height: 879px; overflow: hidden; }
  .produce-backdrop {
    position: absolute; inset: 0;
    background:
      radial-gradient(circle at 12% 20%, var(--tomato-light) 0, transparent 18%),
      radial-gradient(circle at 40% 8%, var(--tomato-light) 0, transparent 14%),
      radial-gradient(circle at 88% 18%, var(--tomato-light) 0, transparent 16%),
      radial-gradient(circle at 10% 62%, var(--tomato-light) 0, transparent 16%),
      radial-gradient(circle at 90% 62%, var(--tomato-light) 0, transparent 15%),
      radial-gradient(circle at 50% 92%, var(--tomato-light) 0, transparent 16%),
      radial-gradient(circle at 85% 92%, var(--tomato-light) 0, transparent 14%),
      linear-gradient(160deg, var(--tomato-red), var(--tomato-deep));
  }
  .label {
    position: absolute; left: 228px; top: 144px; width: 733px; height: 591px;
    background: var(--label-white); border-radius: 38px;
  }
  .label-face {
    position: absolute; left: 18px; top: 18px; right: 18px; bottom: 18px;
    background: var(--label-black); border-radius: 26px; overflow: hidden;
  }
  .gloss-sphere {
    position: absolute; left: 60px; top: -20px; width: 640px; height: 600px; border-radius: 50%;
    background:
      radial-gradient(circle at 78% 78%, rgba(255,255,255,0.7) 0, rgba(255,255,255,0) 12%),
      radial-gradient(circle at 50% 45%, rgba(0,0,0,0.95) 0, rgba(20,20,20,0.9) 55%, rgba(120,120,120,0.55) 85%, rgba(200,200,200,0.2) 100%);
  }
  .tomato-artwork {
    position: absolute; left: -280px; top: 190px; width: 740px; height: 620px;
    border-radius: 50%;
    background: radial-gradient(ellipse at 55% 40%, #e0331f 0, var(--tomato-red) 45%, #b5180f 80%, var(--tomato-deep) 100%);
  }
  .vertical { position: absolute; writing-mode: vertical-rl; white-space: nowrap; }
  .origin-tag {
    left: 523px; top: 36px; width: 60px; height: 258px;
    background: linear-gradient(180deg, var(--gold-light), var(--gold-dark) 55%, var(--gold-light));
    display: flex; align-items: center; justify-content: center;
    font-family: "Shippori Mincho B1", serif; font-weight: 800; font-size: 36px;
    color: var(--ink-dark); letter-spacing: 4px;
  }
  .product-type {
    left: 436px; top: 30px;
    font-family: "Shippori Mincho B1", serif; font-weight: 800; font-size: 40px;
    color: var(--text-white); letter-spacing: 1px;
  }
  .product-name {
    left: 300px; top: 20px;
    font-family: "Kaisei Tokumin", serif; font-weight: 800;
    line-height: 1;
  }
  .product-name .name-kana { color: var(--text-white); font-size: 112px; letter-spacing: 4px; }
  .product-name .name-kanji { color: var(--ink-dark); font-size: 132px; margin-top: 40px; }
</style>
</head>
<body>
<main class="canvas">
  <div class="produce-backdrop" role="img" aria-label="赤く熟したトマトが一面に並ぶ写真"></div>
  <section class="label">
    <div class="label-face">
      <div class="gloss-sphere" role="img" aria-label="光沢のある黒い球体の装飾"></div>
      <div class="tomato-artwork" role="img" aria-label="緑のへたが付いた赤いトマトのイラスト"></div>
      <div class="vertical origin-tag">長崎県壱岐市</div>
      <div class="vertical product-type">高糖度フルーツトマト</div>
      <h1 class="vertical product-name"><span class="name-kana">さほ</span><span class="name-kanji">珠</span></h1>
    </div>
  </section>
</main>
</body>
</html>
```